Plakat-Design
Zielgruppe
Wir bieten Tanzkurse in Salsa, Bachata, Kizomba & Zouk an!
Zielgruppe alle Tanzinteressierten Menschen, bekanntheit steigern und Präsenz zeigen!
Wir bieten in den oben genannten Tänzen mit Spezialisierten internationalen Trainern und Trainerinnen didaktisch & methodisch hochwertige Tanzkurse an.
Wir sind die Führende tanzschuleund in diese Sparte.
Aufgabenstellung
DIN/Maße: Datenblatt im Anhang
Display Roll-Up Classic, 85 cm x 200 cm
Attribute die das Design Repräsentieren sollte:
Professionalität, Eye catcher, Tanz, Bewegung, Dynamik, Jung, Frisch
Es soll edel und farblich harmonisch sein. Keine Chilis, kein Kuban Feeling oder Flamenco-Flair.
Mögliches Bildmaterial ist im Anhang zu finden!
Farbe Logo: #A82068
Weitere verwendete Farben: #0A8694
Ein mitgeliefertes Bild, zeigt mehrere Powder / Aquarell Bilder, ich könnte mir auch etwas in diesem Stil vorstellen, doch dezent!
Inhalte: Bin mir hier leider noch nich abschließend sicher welche Inhalte!
Tanzschule
für Salsa, Bachata, Kizomba & Zouk
Kurse von Anfänger A1 bis Masterclas
Kurse ohne Tanzpartner Buchbar
Flexible Tarife mit Monatlicher Bezahlung
Gratis Schnupperstunde

```html
<!DOCTYPE html>
<html lang="de">
<head>
<meta charset="utf-8">
<title>Baile Vivo – Roll-Up Tanzschule</title>
<link rel="stylesheet" href="https://fonts.googleapis.com/css2?family=Bebas+Neue&family=Roboto+Condensed:wght@400;700&family=Roboto:wght@300;400;500&display=swap">
<style>
  :root {
    --brand-magenta: #A82068;
    --brand-teal: #0A8694;
    --powder-pink: #E8408A;
    --powder-hot: #DE2A7C;
    --powder-soft: #F3A6C8;
    --denim: #5E769C;
    --paper: #F5F3F4;
    --paper-shade: #E6E2E4;
    --text-dark: #2A2428;
    --text-grey: #8A8287;
    --page-bg: #FFFFFF;
  }
  * { box-sizing: border-box; margin: 0; padding: 0; }
  html, body {
    width: 802px; height: 1200px; overflow: hidden;
    background: var(--page-bg);
  }
  .rollup {
    position: absolute;
    left: 161px; top: 35px;
    width: 480px; height: 1130px;
    overflow: hidden;
    background: radial-gradient(ellipse at 50% 40%, #FFFFFF 0%, var(--paper) 55%, var(--paper-shade) 100%);
    font-family: "Roboto Condensed", "Arial Narrow", sans-serif;
  }
  .rollup__swoosh { position: absolute; inset: 0; pointer-events: none; }

  /* Brand name */
  .brand {
    position: absolute; top: 38px; left: 0; width: 100%;
    display: flex; flex-direction: column; align-items: center;
  }
  .brand__row { display: flex; align-items: center; gap: 12px; }
  .brand__name {
    font-weight: 400; font-size: 40px; letter-spacing: 1px;
    color: var(--brand-magenta);
  }
  .brand__dot {
    width: 22px; height: 22px; border-radius: 50%;
    background: var(--brand-magenta);
  }
  .brand__tagline {
    margin-top: 2px;
    font-family: "Roboto", sans-serif; font-weight: 300;
    font-size: 15px; color: var(--text-grey); letter-spacing: .3px;
  }

  /* Photo area */
  .hero-photo {
    position: absolute; left: 0; top: 130px;
    width: 480px; height: 770px;
  }

  /* Headline */
  .headline {
    position: absolute; top: 672px; left: 0; width: 100%;
    text-align: center; color: #FFFFFF;
    font-family: "Bebas Neue", "Oswald", sans-serif;
  }
  .headline__title { font-size: 84px; line-height: 1; letter-spacing: 1px; }
  .headline__styles { margin-top: 2px; font-size: 31px; letter-spacing: .5px; word-spacing: 3px; }
  .headline__styles .sep { font-size: 22px; vertical-align: 3px; margin: 0 2px; }
  .headline__styles .for { margin-right: 18px; }

  /* Benefits */
  .benefits {
    position: absolute; top: 912px; left: 20px; right: 14px;
    list-style: none;
  }
  .benefits li {
    position: relative; padding-left: 24px;
    font-weight: 700; font-size: 18.5px; line-height: 28px;
    color: var(--brand-teal);
  }
  .benefits li::before {
    content: ""; position: absolute; left: 4px; top: 11px;
    width: 6px; height: 6px; border-radius: 50%; background: var(--brand-teal);
  }

  /* Contact */
  .contact {
    position: absolute; top: 1028px; left: 14px; right: 14px;
    display: flex; justify-content: space-between; align-items: flex-start;
    font-family: "Roboto", sans-serif; font-size: 13.5px; color: var(--text-dark);
  }
  .contact__address { width: 225px; text-align: center; line-height: 16px; padding-top: 4px; font-style: normal; }
  .contact__channels { list-style: none; }
  .contact__channels li { display: flex; align-items: center; gap: 10px; height: 27px; }
  .contact__channels svg { width: 18px; height: 18px; flex: none; }
</style>
</head>
<body>
  <main class="rollup">
    <svg class="rollup__swoosh" viewBox="0 0 480 1130" aria-hidden="true">
      <path d="M0 120 C60 40 150 20 240 30" fill="none" stroke="var(--brand-magenta)" stroke-width="1.2" opacity=".5"/>
      <path d="M470 930 C430 1000 400 1060 380 1130" fill="none" stroke="var(--brand-magenta)" stroke-width="1" opacity=".35"/>
    </svg>

    <header class="brand">
      <div class="brand__row">
        <span class="brand__name">Baile Vivo</span>
        <span class="brand__dot"></span>
      </div>
      <p class="brand__tagline">Salsa · Bachata · Kizomba</p>
    </header>

    <svg class="hero-photo" viewBox="0 0 480 770" role="img" aria-label="Foto eines tanzenden Paares in Jeans und weißen Oberteilen, umgeben von einer pinken Aquarell-Pulverwolke">
      <defs>
        <linearGradient id="heroTones" x1="0.15" y1="0" x2="0.75" y2="1">
          <stop offset="0" stop-color="#D8D2DA"/>
          <stop offset="0.3" stop-color="var(--denim)"/>
          <stop offset="0.55" stop-color="var(--powder-soft)"/>
          <stop offset="0.78" stop-color="var(--powder-pink)"/>
          <stop offset="1" stop-color="var(--powder-hot)"/>
        </linearGradient>
        <filter id="powderEdge" x="-5%" y="-5%" width="110%" height="110%">
          <feGaussianBlur stdDeviation="5"/>
        </filter>
      </defs>
      <path filter="url(#powderEdge)" fill="url(#heroTones)"
        d="M70 40 C120 5 220 10 290 70 C370 50 470 100 480 170 L480 690
           C440 750 370 730 300 765 C220 735 130 770 50 740
           C10 725 0 690 0 650 L0 430 C25 320 35 160 70 40 Z"/>
    </svg>

    <section class="headline">
      <h1 class="headline__title">TANZSCHULE</h1>
      <p class="headline__styles"><span class="for">FÜR</span>SALSA <span class="sep">•</span> BACHATA <span class="sep">•</span> KIZOMBA <span class="sep">•</span> ZOUK</p>
    </section>

    <ul class="benefits">
      <li>Kurse für Anfänger bis Fortgeschritten</li>
      <li>Alle Kurse auch ohne Tanzpartner buchbar</li>
      <li>Gratis Schnupperstunde, um uns kennen zu lernen</li>
    </ul>

    <footer class="contact">
      <address class="contact__address">
        Tanzschule im Herzen<br>
        Musterstadts Baile Vivo<br>
        Lindenweg 14 &amp; weitere Locations<br>
        79100 Musterstadt
      </address>
      <ul class="contact__channels">
        <li>
          <svg viewBox="0 0 20 20" fill="none" stroke="var(--brand-magenta)" stroke-width="1.2"><circle cx="10" cy="10" r="8"/><ellipse cx="10" cy="10" rx="3.5" ry="8"/><path d="M2 10h16"/></svg>
          www.baile-vivo-tanz.de
        </li>
        <li>
          <svg viewBox="0 0 20 20" fill="none" stroke="var(--brand-magenta)" stroke-width="1.2"><rect x="2" y="4.5" width="16" height="11"/><path d="M2 4.5l8 6 8-6"/></svg>
          hallo@baile-vivo-tanz.de
        </li>
        <li>
          <svg viewBox="0 0 20 20" fill="none" stroke="var(--brand-magenta)" stroke-width="1.2"><path d="M5 2.5l3 3.5-1.8 2a9 9 0 005.8 5.8l2-1.8 3.5 3-2 2.5C9 17 3 11 2.5 4.5z"/></svg>
          +49 170 000 418 56
        </li>
      </ul>
    </footer>
  </main>
</body>
</html>
```